Patient Engagement Solution

We need an attractive and easy-to-use GUI for patients and clinicians, which includes screens and icons. The application has been named TVNwell. I have our corporate logo attached as well.
I have attached the screens that the developer has used to create the solution, but we all know they miss the target when it comes to the creative stuff.
If it helps, I can supply some competitor's screens as a guide - please let me know.

Target Market(s)

Patients and Clinicians

Industry/Entity Type

Healthcare/Hospitals

Font styles to use
Other font styles liked:
• Easy to Read

Requirements
Must have
• Attractive, easy to use graphical user interface. Screen size is usually 22" 16:9
Nice to have
• Inviting and interesting look
Should not have
• Complicated hard to navigate screens

```html
<!DOCTYPE html>
<html lang="en">
<head>
<meta charset="utf-8">
<title>TVNwell — Patient Engagement Screens</title>
<link href="https://fonts.googleapis.com/css2?family=Inter:wght@400;500;600;700&family=Roboto:ital,wght@1,300&display=swap" rel="stylesheet">
<style>
  :root{
    --stage:#222327;
    --heading:#4b4c52;
    --ink:#1f1f25;
    --ink-soft:#3a3a44;
    --ward:#55566a;
    --chip:rgba(255,255,255,0.72);
    --g-magenta:#e8207a;
    --g-violet:#9c4fe2;
    --g-sun:#ece6a2;
    --g-sky:#3cb9f3;
    --g-pink:#e66ac8;
    --g-lilac:#c9c8f1;
    --g-blue:#66a9f7;
  }
  *{box-sizing:border-box;margin:0;padding:0}
  html,body{width:1200px;height:842px;overflow:hidden;background:var(--stage)}
  body{position:relative;font-family:"Inter",sans-serif;color:var(--ink)}

  .section-title{position:absolute;font-family:"Roboto",sans-serif;font-style:italic;font-weight:300;font-size:19px;color:var(--heading)}

  .screen{position:absolute;width:477px;height:292px;overflow:hidden;
    background:
      radial-gradient(ellipse 45% 60% at 0% 0%, var(--g-magenta) 0%, rgba(232,32,122,0) 100%),
      radial-gradient(ellipse 30% 40% at 0% 100%, var(--g-violet) 0%, rgba(156,79,226,0) 100%),
      radial-gradient(ellipse 45% 55% at 55% 0%, var(--g-sun) 0%, rgba(236,230,162,0) 100%),
      radial-gradient(ellipse 55% 55% at 58% 100%, var(--g-sky) 0%, rgba(60,185,243,0) 100%),
      radial-gradient(ellipse 35% 45% at 10% 70%, var(--g-pink) 0%, rgba(230,106,200,0) 100%),
      radial-gradient(ellipse 40% 50% at 100% 100%, var(--g-blue) 0%, rgba(102,169,247,0) 100%),
      linear-gradient(160deg,#e7b5c8 0%,#ebe2d6 45%,var(--g-lilac) 100%);}
  .screen::after{content:"";position:absolute;inset:8px;border:1.2px solid var(--ink);border-radius:30px;pointer-events:none}

  .pos{position:absolute;transform:translate(-50%,-50%)}
  .icon{width:24px;height:24px;fill:none;stroke:var(--ink);stroke-width:1.6;stroke-linecap:round;stroke-linejoin:round}
  .icon-sm{width:22px;height:22px}

  .menu-label{position:absolute;transform:translateY(-50%);font-size:8px;letter-spacing:.22em;font-weight:500;color:var(--ink)}
  .centered-label{position:absolute;transform:translate(-50%,-50%);font-size:8px;letter-spacing:.18em;font-weight:500;white-space:nowrap}
  .app-label{position:absolute;transform:translate(-50%,-50%);font-size:8px;letter-spacing:.05em;font-weight:500;white-space:nowrap}

  .brand{position:absolute;display:flex;align-items:center;gap:4px;transform:translateY(-50%);font-size:7px;font-weight:700;color:var(--ink)}
  .brand-mark{width:6px;height:6px;background:var(--ink)}

  .bed-info{position:absolute;text-align:right;right:27px}
  .ward{font-size:9px;letter-spacing:.18em;color:var(--ward)}
  .time{font-size:24px;font-weight:400;letter-spacing:-.01em;line-height:1.15;color:var(--ink)}
  .bed{font-size:9px;letter-spacing:.16em;color:var(--ink)}

  .lang-chip{position:absolute;transform:translate(-50%,-50%);width:73px;height:32px;border-radius:9px;background:var(--chip);
    display:flex;align-items:center;justify-content:center;font-size:7.5px;letter-spacing:.08em;font-weight:500}
  .lang-chip.wide{width:76px}
</style>
</head>
<body>

<svg width="0" height="0" style="position:absolute" aria-hidden="true">
  <defs>
    <symbol id="i-home" viewBox="0 0 24 24"><path d="M2.5 11.5 12 3l9.5 8.5M5 9.5V21h5v-6h4v6h5V9.5"/></symbol>
    <symbol id="i-tv" viewBox="0 0 24 24"><rect x="2.5" y="4" width="19" height="12" rx="1"/><path d="M12 16v3M8.5 20.5h7"/></symbol>
    <symbol id="i-radio" viewBox="0 0 24 24"><path d="M9 18V6l11-3v13"/><path d="M9 9l11-3"/><circle cx="6" cy="18" r="3"/><circle cx="17" cy="16" r="3"/></symbol>
    <symbol id="i-apps" viewBox="0 0 24 24"><rect x="3.5" y="3.5" width="7" height="7"/><rect x="13.5" y="3.5" width="7" height="7"/><rect x="3.5" y="13.5" width="7" height="7"/><rect x="13.5" y="13.5" width="7" height="7"/></symbol>
    <symbol id="i-language" viewBox="0 0 24 24"><text x="0" y="19" font-family="Inter, sans-serif" font-size="11" fill="#1f1f25" stroke="none">五</text><text x="11" y="19" font-family="Inter, sans-serif" font-size="17" fill="#1f1f25" stroke="none">a</text></symbol>
    <symbol id="i-clock" viewBox="0 0 24 24"><circle cx="12" cy="12" r="9.5"/><path d="M11 6.5v5.5l3 3"/></symbol>
    <symbol id="i-video" viewBox="0 0 24 24"><rect x="2" y="7" width="14" height="10" rx="1"/><path d="M16 10.5l5.5-3.5v10L16 13.5"/></symbol>
    <symbol id="i-relax" viewBox="0 0 24 24"><path d="M12 20c-4.5 0-8-3-8-8 3 0 6 2 8 5 2-3 5-5 8-5 0 5-3.5 8-8 8z"/><path d="M12 17c-2.2-3-2.2-7.5 0-11 2.2 3.5 2.2 8 0 11z"/></symbol>
    <symbol id="i-internet" viewBox="0 0 24 24"><circle cx="12" cy="12" r="9.5"/><ellipse cx="12" cy="12" rx="4" ry="9.5"/><path d="M2.5 12h19M4 7h16M4 17h16"/></symbol>
    <symbol id="i-clinical" viewBox="0 0 24 24"><rect x="3" y="7" width="18" height="13" rx="1"/><path d="M9 7V4h6v3M12 10.5v6M9 13.5h6"/></symbol>
    <symbol id="i-education" viewBox="0 0 24 24"><path d="M1.5 9.5 12 4.5l10.5 5L12 14.5z"/><path d="M6 11.5v5c3.5 2.5 8.5 2.5 12 0v-5"/></symbol>
    <symbol id="i-meals" viewBox="0 0 24 24"><path d="M4 4l15 16M8 4 5 7l3 3M20 20 6 6"/><path d="M14.5 10c-1.5-2 0-5.5 2.5-6.5 2.5.5 3.5 3 2.5 5.5-1.5 1.5-3.5 2-5 1zM14.5 10 4 20"/></symbol>
    <symbol id="i-books" viewBox="0 0 24 24"><rect x="7" y="2.5" width="12" height="16"/><path d="M4.5 5v16.5h12M10 2.5v16"/></symbol>
    <symbol id="i-concierge" viewBox="0 0 24 24"><path d="M3 19h18M5 19a7 7 0 0 1 14 0M12 9v3M10 9h4"/><path d="M3 4h9M3 4v5M3 7h5"/></symbol>
    <symbol id="i-phone" viewBox="0 0 24 24"><path d="M21 16.5v3a2 2 0 0 1-2.2 2 19.8 19.8 0 0 1-8.6-3.1 19.5 19.5 0 0 1-6-6A19.8 19.8 0 0 1 1.1 3.8 2 2 0 0 1 3.1 1.6h3a2 2 0 0 1 2 1.7c.1 1 .4 1.9.7 2.8a2 2 0 0 1-.5 2.1L7 9.5a16 16 0 0 0 6 6l1.3-1.3a2 2 0 0 1 2.1-.5c.9.3 1.8.6 2.8.7a2 2 0 0 1 1.8 2.1z"/></symbol>
    <symbol id="i-scan" viewBox="0 0 24 24"><path d="M3 8V3h5M16 3h5v5M21 16v5h-5M8 21H3v-5M6 12h12"/></symbol>
    <symbol id="i-games" viewBox="0 0 24 24"><path d="M6 7h12a4 4 0 0 1 4 4l-1 6a2 2 0 0 1-3.5 1L15.5 16h-7L6.5 18A2 2 0 0 1 3 17l-1-6a4 4 0 0 1 4-4z"/><path d="M8 10v4M6 12h4M15.5 11h.01M17.5 13h.01"/></symbol>
    <symbol id="i-movies" viewBox="0 0 24 24"><rect x="3" y="3.5" width="18" height="14" rx="1"/><path d="M10 7.5l5 3-5 3zM9 21h6M12 17.5V21"/></symbol>
    <symbol id="i-heart" viewBox="0 0 24 24"><path d="M20.8 4.6a5.5 5.5 0 0 0-7.8 0L12 5.7l-1-1.1a5.5 5.5 0 0 0-7.8 7.8L12 21.2l8.8-8.8a5.5 5.5 0 0 0 0-7.8z"/><path d="M16.5 7.5a2 2 0 0 1 1.5 2"/></symbol>
    <symbol id="i-gear" viewBox="0 0 24 24"><circle cx="12" cy="12" r="3.2"/><path d="M19.4 15a1.65 1.65 0 0 0 .33 1.82l.06.06a2 2 0 0 1-2.83 2.83l-.06-.06a1.65 1.65 0 0 0-1.82-.33 1.65 1.65 0 0 0-1 1.51V21a2 2 0 0 1-4 0v-.09A1.65 1.65 0 0 0 9 19.4a1.65 1.65 0 0 0-1.82.33l-.06.06a2 2 0 0 1-2.83-2.83l.06-.06a1.65 1.65 0 0 0 .33-1.82 1.65 1.65 0 0 0-1.51-1H3a2 2 0 0 1 0-4h.09A1.65 1.65 0 0 0 4.6 9a1.65 1.65 0 0 0-.33-1.82l-.06-.06a2 2 0 0 1 2.83-2.83l.06.06a1.65 1.65 0 0 0 1.82.33H9a1.65 1.65 0 0 0 1-1.51V3a2 2 0 0 1 4 0v.09a1.65 1.65 0 0 0 1 1.51 1.65 1.65 0 0 0 1.82-.33l.06-.06a2 2 0 0 1 2.83 2.83l-.06.06a1.65 1.65 0 0 0-.33 1.82V9a1.65 1.65 0 0 0 1.51 1H21a2 2 0 0 1 0 4h-.09a1.65 1.65 0 0 0-1.51 1z"/></symbol>
  </defs>
</svg>

<!-- Vertical main menu -->
<h2 class="section-title" style="left:91px;top:58px">Vertical Main Menu</h2>
<section class="screen" style="left:93px;top:98px">
  <svg class="icon pos" style="left:48px;top:48px"><use href="#i-home"/></svg><span class="menu-label" style="left:78px;top:48px">HOME</span>
  <svg class="icon pos" style="left:48px;top:88px"><use href="#i-tv"/></svg><span class="menu-label" style="left:78px;top:88px">TV</span>
  <svg class="icon pos" style="left:48px;top:128px"><use href="#i-radio"/></svg><span class="menu-label" style="left:78px;top:128px">RADIO</span>
  <svg class="icon icon-sm pos" style="left:48px;top:168px"><use href="#i-apps"/></svg><span class="menu-label" style="left:78px;top:168px">APPS</span>
  <svg class="icon pos" style="left:48px;top:210px"><use href="#i-language"/></svg><span class="menu-label" style="left:78px;top:210px">LANGUAGE</span>
  <svg class="icon pos" style="left:48px;top:250px"><use href="#i-clock"/></svg><span class="menu-label" style="left:78px;top:250px">CLOCK</span>
  <div class="brand" style="left:374px;top:33px"><span class="brand-mark"></span>TVNwell</div>
  <div class="bed-info" style="top:205px">
    <p class="ward">Demo Ward</p>
    <p class="time">15:30 AM</p>
    <p class="bed">Default Bed</p>
  </div>
</section>

<!-- Centered main menu -->
<h2 class="section-title" style="left:634px;top:58px">Centered Main Menu</h2>
<section class="screen" style="left:634px;top:98px">
  <svg class="icon pos" style="left:77px;top:140px"><use href="#i-home"/></svg><span class="centered-label" style="left:77px;top:162px">HOME</span>
  <svg class="icon pos" style="left:141px;top:140px"><use href="#i-tv"/></svg><span class="centered-label" style="left:141px;top:162px">TV</span>
  <svg class="icon pos" style="left:206px;top:140px"><use href="#i-radio"/></svg><span class="centered-label" style="left:206px;top:162px">RADIO</span>
  <svg class="icon icon-sm pos" style="left:270px;top:140px"><use href="#i-apps"/></svg><span class="centered-label" style="left:270px;top:162px">APPS</span>
  <svg class="icon pos" style="left:334px;top:140px"><use href="#i-language"/></svg><span class="centered-label" style="left:334px;top:162px">LANGUAGE</span>
  <svg class="icon pos" style="left:402px;top:140px"><use href="#i-clock"/></svg><span class="centered-label" style="left:402px;top:162px">CLOCK</span>
  <div class="brand" style="left:27px;top:259px"><span class="brand-mark"></span>TVNwell</div>
  <div class="bed-info" style="top:207px">
    <p class="ward">Demo Ward</p>
    <p class="time">15:30 AM</p>
    <p class="bed">Default Bed</p>
  </div>
</section>

<!-- Apps menu -->
<h2 class="section-title" style="left:91px;top:434px">Apps Menu</h2>
<section class="screen" style="left:93px;top:476px">
  <svg class="icon pos" style="left:438px;top:38px"><use href="#i-gear"/></svg>

  <svg class="icon pos" style="left:98px;top:101px"><use href="#i-video"/></svg><span class="app-label" style="left:98px;top:126px">Video Calls</span>
  <svg class="icon pos" style="left:145px;top:101px"><use href="#i-relax"/></svg><span class="app-label" style="left:145px;top:126px">Relax</span>
  <svg class="icon pos" style="left:191px;top:101px"><use href="#i-internet"/></svg><span class="app-label" style="left:191px;top:126px">Internet</span>
  <svg class="icon pos" style="left:238px;top:101px"><use href="#i-clinical"/></svg><span class="app-label" style="left:238px;top:126px">Clinical</span>
  <svg class="icon pos" style="left:285px;top:101px"><use href="#i-education"/></svg><span class="app-label" style="left:285px;top:126px">Education</span>
  <svg class="icon pos" style="left:332px;top:101px"><use href="#i-meals"/></svg><span class="app-label" style="left:332px;top:126px">Meals</span>
  <svg class="icon pos" style="left:379px;top:101px"><use href="#i-books"/></svg><span class="app-label" style="left:379px;top:126px">Books</span>

  <svg class="icon icon-sm pos" style="left:96px;top:172px"><use href="#i-apps"/></svg><span class="app-label" style="left:96px;top:199px">Apps</span>
  <svg class="icon pos" style="left:146px;top:172px"><use href="#i-concierge"/></svg><span class="app-label" style="left:146px;top:199px">Concierge</span>
  <svg class="icon pos" style="left:192px;top:172px"><use href="#i-phone"/></svg><span class="app-label" style="left:192px;top:199px">Phone</span>
  <svg class="icon pos" style="left:238px;top:172px"><use href="#i-scan"/></svg><span class="app-label" style="left:238px;top:199px">Barcode</span>
  <svg class="icon pos" style="left:285px;top:172px"><use href="#i-games"/></svg><span class="app-label" style="left:285px;top:199px">Games</span>
  <svg class="icon pos" style="left:332px;top:172px"><use href="#i-movies"/></svg><span class="app-label" style="left:332px;top:199px">Movies</span>
  <svg class="icon pos" style="left:380px;top:172px"><use href="#i-heart"/></svg><span class="app-label" style="left:380px;top:199px">My Care</span>

  <div class="brand" style="left:27px;top:259px"><span class="brand-mark"></span>TVNwell</div>
  <svg class="icon pos" style="left:438px;top:253px;width:26px;height:26px"><use href="#i-home"/></svg>
</section>

<!-- Language selection -->
<h2 class="section-title" style="left:636px;top:434px">Language Selection</h2>
<section class="screen" style="left:634px;top:476px">
  <svg class="icon pos" style="left:438px;top:38px"><use href="#i-gear"/></svg>

  <span class="lang-chip" style="left:158px;top:92px">ENGLISH</span>
  <span class="lang-chip" style="left:239px;top:92px">FRENCH</span>
  <span class="lang-chip" style="left:321px;top:92px">JAPANESE</span>
  <span class="lang-chip" style="left:158px;top:134px">ITALIAN</span>
  <span class="lang-chip" style="left:239px;top:134px">SPANISH</span>
  <span class="lang-chip" style="left:321px;top:134px">CHINESE</span>
  <span class="lang-chip" style="left:158px;top:176px">GERMAN</span>
  <span class="lang-chip" style="left:239px;top:176px">HINDI</span>
  <span class="lang-chip" style="left:321px;top:176px">ARABIC</span>
  <span class="lang-chip wide" style="left:241px;top:217px">VIETNAMESE</span>

  <div class="brand" style="left:27px;top:259px"><span class="brand-mark"></span>TVNwell</div>
  <svg class="icon pos" style="left:438px;top:253px;width:26px;height:26px"><use href="#i-home"/></svg>
</section>

</body>
</html>
```